Signage setout with photos for side of Mowing Trailer

We need signage for our mowing trailer to attract new business.
Specifically a Rear sign 1470x880mm and Side signs 2400x880mm
Sign needs to be modern and professional.
Some example uploads as to what we have thought about so far.
Logo doesn't need to be the green colour.
Logo words and Logo of Mower do not need to be together.
Link to get a mower image>
https://bluefernmachinery.com/torvo
Updates

Need extra days to review

Target Market(s)

Other Customers driving past the trailer.

Industry/Entity Type

Lawnmowing / Landscaping

Requirements
Must have
• Phone Number, Company Name & Logo, Web address, Facebook and Insta Logos, Comment - "Acreage & Commercial Specialists" Catchcry - "100% Electric Mowing Company - est 2017" Services "Mowing, Hedging, Pressure Cleaning, Weed Control, Fencing, Turfing, Mulching and Rubbish Removal"
Nice to have
• Full colour background images.

```html
<!DOCTYPE html>
<html lang="en">
<head>
<meta charset="utf-8">
<title>Fresh Turf Mowing – Trailer Signage</title>
<link href="https://fonts.googleapis.com/css2?family=Poppins:ital,wght@0,600;0,700;1,700;1,800;1,900&family=Hind:wght@600&family=Barlow+Condensed:wght@600&display=swap" rel="stylesheet">
<style>
  :root{
    --bg:#c9cacc;
    --bg-dark:#b9babd;
    --green-deep:#1c6b32;
    --green-mid:#2f8a2f;
    --green-light:#5fae3a;
    --mower:#3a8a2a;
    --orange:#f26a21;
    --white:#ffffff;
    --ink:#111111;
  }
  *{margin:0;padding:0;box-sizing:border-box}
  html,body{width:1200px;height:933px;overflow:hidden}
  body{
    position:relative;
    background:linear-gradient(150deg,var(--bg) 0%,var(--bg) 55%,var(--bg-dark) 55%,var(--bg-dark) 100%);
    font-family:"Poppins",sans-serif;
  }
  .size-label{
    position:absolute;left:0;width:1200px;text-align:center;
    font-family:"Poppins",sans-serif;font-weight:600;font-size:40px;color:var(--ink);
  }
  .size-label--rear{top:42px}
  .size-label--side{top:836px}

  .sign{position:absolute;overflow:hidden;background:var(--white);box-shadow:2px 3px 6px rgba(0,0,0,.35)}
  .sign--rear{left:320px;top:117px;width:560px;height:335px}
  .sign--side{left:142px;top:480px;width:916px;height:335px}

  .sign__field{position:absolute;inset:0}
  .sign__photo-mower{position:absolute;border-radius:10px;
    background:linear-gradient(180deg,#4b6b3d 0%,var(--mower) 55%,#2b6a20 100%)}
  .sign__photo-grass{position:absolute;left:0;right:0;
    background:linear-gradient(180deg,rgba(95,174,58,0) 0%,#4c9c2e 45%,#3b8a26 100%)}

  .services-band{position:absolute;left:0;top:0;right:0;height:30px;background:var(--green-deep);
    color:var(--white);font-family:"Barlow Condensed",sans-serif;font-weight:600;font-size:13px;
    display:flex;align-items:center;justify-content:center;letter-spacing:.1px}
  .web-band{position:absolute;left:0;right:0;bottom:0;background:var(--green-deep);color:var(--white);
    font-weight:700;text-align:center;letter-spacing:3px;display:flex;align-items:center;justify-content:center}
  .sign--rear .web-band{height:28px;font-size:15px}
  .sign--side .web-band{height:39px;font-size:19px}

  .brand{position:absolute;background:var(--white);border-radius:0 0 12px 12px;
    display:flex;flex-direction:column;align-items:center;justify-content:center;
    font-family:"Hind",sans-serif;font-weight:600;color:var(--green-deep);line-height:.95;text-align:center}
  .brand__dot{position:absolute;border-radius:50%;background:var(--orange)}
  .sign--rear .brand{left:26px;top:97px;width:164px;height:53px;font-size:18px}
  .sign--rear .brand__dot{width:28px;height:28px;left:42px;top:-42px}
  .sign--side .brand{left:35px;top:72px;width:200px;height:72px;font-size:24px}
  .sign--side .brand__dot{width:34px;height:34px;left:60px;top:-52px}
  .brand__big{font-size:1.3em}

  .tagline{position:absolute;color:var(--white);font-weight:800;font-style:italic;text-align:center;
    line-height:1.02;text-shadow:1px 2px 3px rgba(0,0,0,.55)}
  .sign--rear .tagline{left:18px;top:180px;width:190px;font-size:25px}
  .sign--side .tagline{left:26px;top:160px;width:192px;font-size:28px}

  .phone{position:absolute;color:var(--white);font-weight:800;font-style:italic;
    text-shadow:1px 2px 3px rgba(0,0,0,.5);white-space:nowrap;line-height:1}
  .sign--rear .phone{left:370px;top:127px;font-size:31px}
  .sign--side .phone{left:482px;top:112px;font-size:36px}

  .social{position:absolute;display:flex;gap:6px}
  .social__slot{border:2px solid var(--ink);border-radius:50%;background:rgba(255,255,255,.85)}
  .sign--rear .social{left:424px;top:163px}
  .sign--rear .social__slot{width:27px;height:27px}
  .sign--side .social{left:545px;top:155px}
  .sign--side .social__slot{width:32px;height:32px}

  .services{position:absolute;left:696px;top:106px;color:var(--white);text-shadow:1px 1px 2px rgba(0,0,0,.5)}
  .services__title{font-weight:700;font-size:25px;letter-spacing:.5px}
  .services__list{list-style:none;font-family:"Barlow Condensed",sans-serif;font-weight:600;font-size:16px;line-height:19.5px}

  .catchcry{position:absolute;left:0;right:0;text-align:center;color:var(--orange);font-weight:900;font-style:italic;
    text-shadow:-1px -1px 0 #fff,1px -1px 0 #fff,-1px 1px 0 #fff,1px 1px 0 #fff,0 2px 4px rgba(0,0,0,.4)}
  .sign--rear .catchcry{top:278px;font-size:20px}
  .sign--side .catchcry{top:260px;font-size:27px}
</style>
</head>
<body>
  <div class="size-label size-label--rear">1470x880mm</div>

  <section class="sign sign--rear">
    <svg class="sign__field" viewBox="0 0 560 335" width="560" height="335" role="img" aria-label="Striped green lawn rolling under a white sky band">
      <defs>
        <linearGradient id="lawnRear" x1="0" y1="0" x2="1" y2="1">
          <stop offset="0" stop-color="#3f8f2c"/><stop offset=".5" stop-color="#2d7a25"/><stop offset="1" stop-color="#4a9a30"/>
        </linearGradient>
      </defs>
      <path d="M0 95 Q60 92 140 110 Q300 130 420 90 Q500 66 560 80 L560 335 L0 335 Z" fill="url(#lawnRear)"/>
      <path d="M0 95 Q60 92 140 110 Q300 130 420 90 Q500 66 560 80" fill="none" stroke="var(--green-deep)" stroke-width="6"/>
    </svg>
    <div class="sign__photo-grass" style="top:230px;height:80px" role="img" aria-label="Close-up of long grass blades"></div>
    <div class="sign__photo-mower" style="left:206px;top:50px;width:154px;height:225px" role="img" aria-label="Man driving a green electric ride-on zero-turn mower"></div>

    <div class="services-band">• Mowing • Hedging • Pressure Cleaning • Weed Control • Fencing • Turfing • Mulching • Rubbish Removal</div>

    <div class="brand"><span class="brand__dot"></span><span>FRESH TURF</span><span class="brand__big">MOWING</span></div>
    <p class="tagline">Acreage &amp;<br>Commercial<br>Specialists</p>
    <p class="phone">3790-4126</p>
    <div class="social"><span class="social__slot"></span><span class="social__slot"></span></div>
    <p class="catchcry">100% Electric Mowing Company - est 2017</p>
    <div class="web-band">www.freshturfmowing.com.au</div>
  </section>

  <section class="sign sign--side">
    <svg class="sign__field" viewBox="0 0 916 335" width="916" height="335" role="img" aria-label="Striped green lawn rolling under a white sky band">
      <defs>
        <linearGradient id="lawnSide" x1="0" y1="0" x2="1" y2="1">
          <stop offset="0" stop-color="#3f8f2c"/><stop offset=".5" stop-color="#2d7a25"/><stop offset="1" stop-color="#4a9a30"/>
        </linearGradient>
      </defs>
      <path d="M0 95 Q80 110 220 140 Q420 170 600 90 Q760 40 916 120 L916 335 L0 335 Z" fill="url(#lawnSide)"/>
      <path d="M0 95 Q80 110 220 140 Q420 170 600 90 Q760 40 916 120" fill="none" stroke="var(--green-deep)" stroke-width="7"/>
    </svg>
    <div class="sign__photo-grass" style="top:225px;height:75px" role="img" aria-label="Close-up of long grass blades"></div>
    <div class="sign__photo-mower" style="left:266px;top:16px;width:204px;height:240px" role="img" aria-label="Man driving a green electric ride-on zero-turn mower"></div>

    <div class="brand"><span class="brand__dot"></span><span>FRESH TURF</span><span class="brand__big">MOWING</span></div>
    <p class="tagline">Acreage &amp;<br>Commercial<br>Specialists</p>
    <p class="phone">3790-4126</p>
    <div class="social"><span class="social__slot"></span><span class="social__slot"></span></div>
    <div class="services">
      <p class="services__title">SERVICES</p>
      <ul class="services__list">
        <li>• Mowing • Hedging</li>
        <li>• Pressure Cleaning</li>
        <li>• Weed Control</li>
        <li>• Fencing • Turfing</li>
        <li>• Mulching • Rubbish Removal</li>
      </ul>
    </div>
    <p class="catchcry">100% Electric Mowing Company - est 2017</p>
    <div class="web-band">www.freshturfmowing.com.au</div>
  </section>

  <div class="size-label size-label--side">2400x880mm</div>
</body>
</html>
```